Quillmere Surgical Clinic ,Perth- Australia

We need a letterhead for our surgical clinic , it needs to highlight all the relevant contact details and practice locations. needs to be eye catching, but remain professional.all the logos attached
clear contact details as follows

Surgeon name : Mr Tevin Oskard
Phone : 1300 482 917 - 0417 296 481
Fax : 08- 7524 3968
email : tevin@parvellaclinicgroup.com.au
www.parvellaclinicgroup.com.au

Consults from
1- Haldane Medical Centre - Level 3 - Suite 42.
9 Cotterill Vance Parade
Murdoch WA 6157

2- KBRT Mandurah Suites
54 Pellingham Road Mandurah 6214

Operates at :
Our Lady of Peace Murdoch Hospital
Doreen Whitcombe Hospital
Tarn Health Campus
Rookwell Hospital
Ravenfield Hopital
Our Lady of Peace Subiaco

Target Market(s)

General Practitioners (Family doctors)

Industry/Entity Type

Medical

Requirements
Must have
• all the logos attached
• clear contact details as follows
• Surgeon name : Mr Tevin Oskard
• Phone : 1300 482 917 - 0417 296 481
• Fax : 08- 7524 3968
• email : tevin@parvellaclinicgroup.com.au
• www.parvellaclinicgroup.com.au
• Consults from
• 1- Haldane Medical Centre - Level 3 - Suite 42.
• 9 Cotterill Vance Parade
• Murdoch WA 6157
• 2- KBRT Mandurah Suites
• 54 Pellingham Road Mandurah 6214
• Operates at :
• Our Lady of Peace Murdoch Hospital
• Doreen Whitcombe Hospital
• Tarn Health Campus
• Rookwell Hospital
• Ravenfield Hopital
• Our Lady of Peace Subiaco
Nice to have
• a surgical theme in the design , but remain professional
Should not have
• big chunky designs
• no photographs or diagrams of objects (ECG, or stethoscope ..ect)

```html
<!DOCTYPE html>
<html lang="en">
<head>
<meta charset="utf-8">
<title>Quillmere Surgical Clinic – Letterhead</title>
<link rel="stylesheet" href="https://fonts.googleapis.com/css2?family=Arimo:wght@400;700&display=swap">
<style>
  :root {
    --bg: #ececec;
    --paper: #f7f7f7;
    --teal: #5fb3b3;
    --navy: #2d5f93;
    --tan: #c4995f;
    --ink: #555a5e;
    --faint: #e3e8ea;
    --badge: #c9cfd3;
  }
  * { box-sizing: border-box; margin: 0; padding: 0; }
  html, body { width: 1200px; height: 795px; overflow: hidden; background: var(--bg); font-family: "Arimo", Arial, sans-serif; }
  .letterhead {
    position: absolute; left: 330px; top: 18px;
    width: 540px; height: 760px;
    background: var(--paper);
    box-shadow: 0 2px 10px rgba(0,0,0,.12);
    overflow: hidden; color: var(--ink);
  }
  .brand { position: absolute; left: 34px; top: 34px; display: flex; align-items: center; gap: 12px; }
  .brand-mark { width: 44px; height: 44px; border-radius: 50%; border: 4px solid #a9cbd8; }
  .brand-name { color: var(--navy); font-size: 12.5px; letter-spacing: 2.4px; line-height: 1.25; text-transform: uppercase; }
  .surgeon { position: absolute; left: 34px; top: 100px; font-size: 9px; line-height: 1.5; }
  .surgeon-name { color: var(--tan); font-size: 11px; }
  .practice { position: absolute; left: 258px; top: 34px; width: 250px; font-size: 7.6px; line-height: 1.45; }
  .section-title { color: var(--tan); font-size: 9px; text-transform: uppercase; margin-bottom: 4px; }
  .consults { display: flex; border-top: 1px solid var(--teal); padding-top: 5px; margin-bottom: 12px; }
  .consults address { font-style: normal; flex: 1; padding-right: 8px; }
  .consults address + address { border-left: 1px solid var(--teal); padding-left: 8px; }
  .operates p { margin: 0; }
  .header-rule { position: absolute; left: 34px; right: 32px; top: 150px; border-top: 1px solid var(--teal); }
  .watermark { position: absolute; left: 120px; top: 230px; width: 300px; height: 300px; border-radius: 50%; background: radial-gradient(circle, #eef0ee 0 55%, var(--faint) 56% 66%, transparent 67%); }
  .badges { position: absolute; left: 40px; right: 40px; bottom: 100px; display: flex; justify-content: space-between; align-items: center; }
  .badge { background: var(--badge); }
  .badge.sq { width: 26px; height: 26px; }
  .badge.rect { width: 44px; height: 20px; }
  .badge.circle { width: 26px; height: 26px; border-radius: 50%; }
  .contact-band {
    position: absolute; left: 0; right: 0; bottom: 0; height: 78px; background: var(--teal);
    color: #fff; display: flex; align-items: center; padding: 0 24px; gap: 16px; font-size: 9.5px; line-height: 1.6;
  }
  .contact-group { display: flex; flex-direction: column; }
  .contact-line { display: flex; align-items: center; gap: 5px; }
  .contact-line svg { width: 9px; height: 9px; fill: #fff; flex: none; }
  .divider { width: 1px; height: 36px; background: rgba(255,255,255,.7); }
  .band-brand { margin-left: auto; font-size: 8px; letter-spacing: 1px; text-transform: uppercase; text-align: right; }
</style>
</head>
<body>
<main class="letterhead">
  <header>
    <div class="brand">
      <span class="brand-mark"></span>
      <div class="brand-name">Quillmere<br>Surgical<br>Clinic</div>
    </div>
    <div class="surgeon">
      <div class="surgeon-name">Mr Tevin Oskard</div>
      <div>Endocrine, Breast and General Surgeon</div>
      <div>Our Lady of Peace Murdoch Hospital</div>
    </div>
    <section class="practice">
      <h2 class="section-title">Consults from</h2>
      <div class="consults">
        <address>KBRT Mandurah Suites<br>54 Pellingham Road<br>Mandurah 6214</address>
        <address>Haldane Medical Centre<br>Level 3 - Suite 42.<br>9 Cotterill Vance Parade<br>Murdoch WA 6157</address>
      </div>
      <h2 class="section-title">Operates at :</h2>
      <div class="operates">
        <p>Doreen Whitcombe Hospital | Tarn Health Campus | Rookwell Hospital</p>
        <p>Ravenfield Hopital | Our Lady of Peace Subiaco</p>
      </div>
    </section>
    <div class="header-rule"></div>
  </header>

  <div class="watermark" role="img" aria-label="Faint enlarged clinic emblem as background decoration"></div>

  <div class="badges" aria-label="Professional affiliations">
    <span class="badge sq"></span>
    <span class="badge rect"></span>
    <span class="badge circle"></span>
    <span class="badge rect"></span>
    <span class="badge sq"></span>
    <span class="badge circle"></span>
    <span class="badge rect"></span>
    <span class="badge circle"></span>
  </div>

  <footer class="contact-band">
    <div class="contact-group">
      <span class="contact-line"><svg viewBox="0 0 10 10"><path d="M2 0.5 L3.6 2.6 2.8 3.6 C3.4 5 5 6.6 6.4 7.2 L7.4 6.4 9.5 8 8.6 9.4 C4.5 9.4 0.6 5.5 0.6 1.4Z"/></svg>1300 482 917</span>
      <span class="contact-line"><svg viewBox="0 0 10 10"><path d="M2 0.5 L3.6 2.6 2.8 3.6 C3.4 5 5 6.6 6.4 7.2 L7.4 6.4 9.5 8 8.6 9.4 C4.5 9.4 0.6 5.5 0.6 1.4Z"/></svg>0417 296 481</span>
    </div>
    <span class="divider"></span>
    <div class="contact-group">
      <span class="contact-line"><svg viewBox="0 0 10 10"><rect x="2" y="0.5" width="6" height="3"/><rect x="0.5" y="4" width="9" height="5"/></svg>08- 7524 3968</span>
    </div>
    <span class="divider"></span>
    <div class="contact-group">
      <span class="contact-line"><svg viewBox="0 0 10 10"><path d="M0.5 2 H9.5 V8.5 H0.5Z M1 2.5 L5 5.5 9 2.5" fill="none" stroke="#fff"/></svg>tevin@parvellaclinicgroup.com.au</span>
      <span class="contact-line"><svg viewBox="0 0 10 10"><circle cx="5" cy="5" r="4.3" fill="none" stroke="#fff"/><path d="M0.7 5 H9.3 M5 0.7 C2.5 3 2.5 7 5 9.3 M5 0.7 C7.5 3 7.5 7 5 9.3" fill="none" stroke="#fff" stroke-width=".7"/></svg>www.parvellaclinicgroup.com.au</span>
    </div>
    <div class="band-brand">Quillmere</div>
  </footer>
</main>
</body>
</html>
```